Landing page needed for existing website. High Converting SaaS Landing Page!

Landing page needed for existing website. www.slotnudge.com.au

*Must be designed with Framelace framework in mind (so it looks great across all devices).
* Target market is small business owners who take many appointments each day. They want to reduce no shows and remind their customers of appointments dates and times.
* Highlight we intregrate into Plimber Planner, Tessaway Planner, Or use our Build in Web Calendar
* Competitors (vexmoro.com, bookingbellwise.org)
* Clean modern fresh.
* http://kelvarncrafts.com/portfolio_category/web-design/ for inspiration
* Must have link for existing customers to login
* Navigation for future pages.
* Footer section for links to other pages (maybe a contact form)
* The aim of the page is to get prospects to start a Free trial.
* We have 3 domains. slotnudge.com.au (australian customers) slotnudge.co.nz (new zealand customers). slotnudge.info (US customers) these should be linked somewhere. Maybe in the footer with little flags.
Open to ideas on how the page should look. I would prefer something reasonably long with strong imagery.

Target Market(s)

Busy self employer business owners who have many appointments each day. Health professionals, Coaches, Financial Advisers, Tax Lawyers etc etc

Industry/Entity Type

Saas

Number of Pages Required

2 page

Font styles to use
Sans Serif

Requirements
Must have
• 1- Strong Landing Page.
• 2- Stripped down 2nd page that can be used for content, blog posts, content etc.
Nice to have
• Pricing Table

```html
<!DOCTYPE html>
<html lang="en">
<head>
<meta charset="utf-8">
<title>SlotNudge — Automated Reminder System</title>
<link href="https://fonts.googleapis.com/css2?family=Open+Sans:ital,wght@0,400;0,600;0,700;1,700&family=Titillium+Web:ital,wght@0,600;0,700;1,700&display=swap" rel="stylesheet">
<style>
:root{
  --green:#5dba5d;
  --green-dark:#4aa54a;
  --green-light:#8fd18f;
  --blue:#2fb6ea;
  --ink:#2b2b2b;
  --muted:#555;
  --light:#f1f1f1;
  --white:#fff;
  --slate:#34495e;
}
*{box-sizing:border-box;margin:0;padding:0}
html,body{width:1200px;height:4737px;overflow:hidden}
body{font-family:"Open Sans",Arial,sans-serif;color:var(--ink);background:var(--white)}
a{text-decoration:none;color:inherit}

/* header */
.site-header{height:164px;position:relative;background:var(--white)}
.brand{position:absolute;left:50px;top:44px;display:flex;align-items:center;gap:14px}
.brand-dot{width:58px;height:58px;border-radius:50%;background:var(--green)}
.brand-name{font-family:"Titillium Web",sans-serif;font-weight:700;font-size:34px;color:var(--ink)}
.account-links{position:absolute;right:50px;top:38px;display:flex;gap:14px}
.pill{background:var(--green);color:var(--white);font-weight:700;font-size:15px;padding:8px 20px;border-radius:6px;display:flex;align-items:center;gap:8px}
.pill svg{width:16px;height:16px}
.main-nav{position:absolute;right:50px;top:124px;display:flex;gap:24px;font-size:14px;font-weight:600;color:var(--green);text-transform:uppercase}

/* hero */
.hero{height:524px;position:relative;background:linear-gradient(180deg,#6b6b6b 0%,#4a4a4a 45%,#2c2c2c 100%);color:var(--white);text-align:center}
.hero-title{position:absolute;top:180px;left:0;right:0;font-family:"Titillium Web",sans-serif;font-weight:700;font-size:38px;line-height:46px;letter-spacing:.5px}
.hero-sub{position:absolute;top:228px;left:0;right:0;font-weight:600;font-size:21px;line-height:28px}
.cta-row{display:flex;justify-content:center;gap:24px}
.hero .cta-row{position:absolute;left:0;right:0;top:290px}
.btn{display:inline-block;color:var(--white);font-weight:700;font-size:19px;text-transform:uppercase;padding:10px 26px}
.btn-tour{background:var(--green)}
.btn-trial{background:var(--blue)}

/* integrations */
.integrations{height:402px;background:var(--green);color:var(--white);position:relative}
.integrations-strip{height:92px;background:var(--green-light);display:flex;align-items:center;justify-content:center;font-family:"Titillium Web",sans-serif;font-weight:700;font-size:32px}
.integration-list{display:flex;justify-content:center;gap:80px;margin-top:52px}
.integration{width:200px;text-align:center;font-weight:600;font-size:18px}
.integration-ring{width:176px;height:176px;border-radius:50%;margin:0 auto 16px;border:8px solid var(--white);background:var(--green-dark);box-shadow:0 0 0 4px #c7ecc7;display:flex;align-items:center;justify-content:center}
.integration-ring svg{width:80px;height:80px}

/* how it works */
.how{height:505px;position:relative;text-align:center}
.section-title{font-family:"Titillium Web",sans-serif;font-style:italic;font-weight:700;font-size:32px;line-height:40px;color:var(--green);text-transform:uppercase}
.how .section-title{padding-top:16px}
.video{position:absolute;left:253px;top:76px;width:695px;height:395px;background:linear-gradient(180deg,var(--slate) 0,var(--slate) 14%,#eef2f5 14%,#dfe6ea 100%)}
.play{position:absolute;left:50%;top:50%;transform:translate(-50%,-50%);width:90px;height:90px}

/* audience band */
.audience{height:173px;background:var(--green);text-align:center;color:var(--ink)}
.audience .section-title{color:var(--white);padding-top:28px}
.audience p{font-weight:700;font-size:16px;line-height:26px;margin-top:14px;padding:0 200px}

/* features */
.feature{height:221px;position:relative;overflow:hidden}
.feature-photo{position:absolute;top:0;height:221px;width:640px}
.feature.photo-left .feature-photo{left:0;clip-path:polygon(0 0,100% 0,86% 100%,0 100%)}
.feature.photo-right .feature-photo{right:0;clip-path:polygon(14% 0,100% 0,100% 100%,0 100%)}
.feature-text{position:absolute;top:34px;width:500px}
.feature.photo-left .feature-text{left:640px}
.feature.photo-right .feature-text{left:58px}
.feature h3{font-size:20px;font-weight:700}
.feature h4{font-size:16px;font-weight:700;margin-bottom:14px}
.feature h3 + p{margin-top:14px}
.feature p{font-size:15px;line-height:22px;color:var(--muted)}

/* pricing */
.pricing{height:521px;background:var(--green);position:relative;text-align:center}
.pricing .section-title{color:var(--white);padding-top:32px}
.plans{position:absolute;top:88px;left:57px;right:32px;display:flex;gap:16px}
.plan{width:268px;background:var(--white);padding:10px}
.plan-name{background:var(--green);color:var(--white);font-weight:700;font-size:18px;padding:10px 0;text-transform:uppercase}
.plan-row{font-size:16px;font-weight:600;padding:10px 0;border-bottom:1px solid #ddd}
.plan-row:nth-child(odd){background:var(--light)}
.plan-price{font-weight:700}
.plan-order{background:var(--green);margin-top:10px;padding:16px 0}
.plan-order span{display:inline-block;border:2px solid var(--white);color:var(--white);font-weight:700;font-size:15px;padding:6px 22px}

/* testimonials */
.testimonials{height:379px;background:var(--green);position:relative;border-top:16px solid var(--white);text-align:center}
.testimonials .section-title{color:var(--white);padding-top:22px}
.client{position:absolute;background:var(--white);text-align:center}
.client-photo{border-radius:50%;background:linear-gradient(135deg,#d9d9d9,#9a9a9a);margin:0 auto;border:5px solid #e9e9e9}
.client-small{top:130px;width:170px;height:190px;padding-top:20px}
.client-small .client-photo{width:108px;height:108px}
.client-small .client-label{margin-top:14px;font-size:12px;color:var(--white);background:var(--green-light);padding:3px 0}
.client-main{left:250px;top:100px;width:220px;height:240px;padding-top:24px;box-shadow:0 4px 14px rgba(0,0,0,.2)}
.client-main .client-photo{width:140px;height:140px}
.client-main .client-label{margin-top:18px;background:#2e4a2e;color:var(--white);font-weight:700;font-size:18px;padding:8px 0}
.quote{position:absolute;left:720px;top:136px;width:400px;text-align:left;color:var(--white);font-size:15px;line-height:22px;font-style:italic}
.quote cite{display:block;margin-top:18px;font-style:normal;font-weight:700;font-size:16px}

/* guarantee */
.guarantee{height:268px;text-align:center;padding-top:40px}
.guarantee p{font-weight:600;font-size:17px;line-height:26px;margin:18px auto 22px;width:900px}

/* footer */
.site-footer{height:253px;background:var(--light);position:relative;font-size:13px;color:var(--ink)}
.footer-about{position:absolute;left:76px;top:34px;width:300px;line-height:18px}
.flags{display:flex;gap:12px;margin-top:16px}
.flag{width:40px;height:26px}
.footer-col{position:absolute;top:34px;line-height:18px}
.footer-col h5{color:var(--green);font-size:12px;font-weight:700;text-transform:uppercase;margin-bottom:10px}
.footer-brand{position:absolute;right:80px;top:40px;display:flex;align-items:center;gap:10px}
.footer-brand .brand-dot{width:40px;height:40px}
.footer-brand .brand-name{font-size:24px}
.copyright{position:absolute;bottom:0;left:0;right:0;height:46px;border-top:1px solid #ccc;display:flex;align-items:center;justify-content:center;font-size:11px;font-weight:600}
</style>
</head>
<body>

<header class="site-header">
  <a class="brand" href="#"><span class="brand-dot"></span><span class="brand-name">SlotNudge</span></a>
  <div class="account-links">
    <a class="pill" href="#"><svg viewBox="0 0 16 16"><circle cx="8" cy="8" r="7" fill="#fff"/><path d="M6 4l4 4-4 4" stroke="#5dba5d" stroke-width="2" fill="none"/></svg>LOGIN</a>
    <a class="pill" href="#"><svg viewBox="0 0 16 16"><circle cx="8" cy="8" r="7" fill="#fff"/><path d="M6 4l4 4-4 4" stroke="#5dba5d" stroke-width="2" fill="none"/></svg>START FREE TRIAL</a>
  </div>
  <nav class="main-nav">
    <a href="#">Appointment Calendar</a><a href="#">Plimber Planner</a><a href="#">Tessaway Planner</a><a href="#">Blog</a><a href="#">Contact</a>
  </nav>
</header>

<section class="hero" role="img" aria-label="Business people walking on a city street">
  <h1 class="hero-title">AUTOMATED REMINDER SYSTEM AND MESSAGE SERVICE</h1>
  <p class="hero-sub">Reduce your customer no-shows and remind your customers of the important details.</p>
  <div class="cta-row">
    <a class="btn btn-tour" href="#">Take a Tour</a>
    <a class="btn btn-trial" href="#">Try SlotNudge for Free</a>
  </div>
</section>

<section class="integrations">
  <h2 class="integrations-strip">Use The SlotNudge Calendar Or Connect To Your Existing Calendar</h2>
  <div class="integration-list">
    <div class="integration"><div class="integration-ring"><svg viewBox="0 0 80 80"><path d="M24 56h32l-5-8V34a11 11 0 0 0-22 0v14z" fill="none" stroke="#fff" stroke-width="4"/><circle cx="40" cy="62" r="4" fill="#fff"/></svg></div>SlotNudge Calendar</div>
    <div class="integration"><div class="integration-ring"><svg viewBox="0 0 80 80"><rect x="16" y="20" width="48" height="44" rx="3" fill="none" stroke="#fff" stroke-width="4"/><path d="M16 32h48M28 14v12M52 14v12" stroke="#fff" stroke-width="4"/><path d="M26 42h8M38 42h8M50 42h6M26 52h8M38 52h8" stroke="#fff" stroke-width="3"/></svg></div>Plimber Planner</div>
    <div class="integration"><div class="integration-ring"><svg viewBox="0 0 80 80"><rect x="16" y="18" width="48" height="44" rx="4" fill="none" stroke="#fff" stroke-width="4"/><path d="M16 30h48M30 18v44" stroke="#fff" stroke-width="3"/></svg></div>Tessaway Planner</div>
    <div class="integration"><div class="integration-ring"><svg viewBox="0 0 80 80"><path d="M22 12h26l12 12v44H22z" fill="none" stroke="#fff" stroke-width="4"/><path d="M30 36h22M30 46h22M30 56h16" stroke="#fff" stroke-width="3"/></svg></div>CSV File</div>
  </div>
</section>

<section class="how">
  <h2 class="section-title">How It Works</h2>
  <div class="video" role="img" aria-label="Video preview of the SlotNudge calendar screen">
    <svg class="play" viewBox="0 0 90 90"><circle cx="45" cy="45" r="43" fill="rgba(43,43,43,.7)" stroke="#fff" stroke-width="3"/><path d="M36 28l26 17-26 17z" fill="#fff"/></svg>
  </div>
</section>

<section class="audience">
  <h2 class="section-title">Built For Professional Services Businesses</h2>
  <p>Health Professionals, Lawyers, Accountants, Financial Advisers, Coaches, Fitness Trainers, Dentists, Driving Instructors, Training Organisations, Schools.</p>
</section>

<section class="features">
  <article class="feature photo-left">
    <div class="feature-photo" role="img" aria-label="Hand holding a mobile phone" style="background:linear-gradient(120deg,#d8d8d8,#8c8c8c)"></div>
    <div class="feature-text"><h3>SMS &amp; Text Reminders</h3><h4>Text Messages have an over 90% open rate.</h4><p>Meaning your reminder is very likely to be read and noted. It's better to know when a customer isn't able to make, rather than just no showing up. It's far more convient for customers to reply to a text message than having to call and interupting your workflow.</p></div>
  </article>
  <article class="feature photo-right">
    <div class="feature-text"><h3>Email Reminders</h3><h4>Send Timely Email Reminders</h4><p>Email reminders allow you a bit more flexability than text and voice reminders. They allow you send more information about the appointment and even include a map to your location. Why not send a Email and Text Reminder at the same time?</p></div>
    <div class="feature-photo" role="img" aria-label="Laptop keyboard with an email symbol" style="background:linear-gradient(120deg,#bfbfbf,#3a3a3a)"></div>
  </article>
  <article class="feature photo-left">
    <div class="feature-photo" role="img" aria-label="Person holding a phone to their ear" style="background:linear-gradient(120deg,#c9a27a,#5a3d28)"></div>
    <div class="feature-text"><h3>Voice Reminders</h3><h4>Send Scripted Voicemail</h4><p>Voice reminders are still a popular choice for many of our customers. Voice reminders like text messages have a very high rate of engagement, meaning if someone is unable to make an appointment they are likely to let you know.</p></div>
  </article>
  <article class="feature photo-right">
    <div class="feature-text"><h3>Multiple Reminder Scripts</h3><p>You're not limited to using the same script for each reminder. You may have multiple staff and you'd like to mention there name in the script. No problem. You may also want to use a diffent script depending on the service your client is receiving. Or you might have different locations and want to mention the location in their reminder message.</p></div>
    <div class="feature-photo" role="img" aria-label="Printed charts and documents on a desk" style="background:linear-gradient(120deg,#eef1f4,#aab4be)"></div>
  </article>
  <article class="feature photo-left">
    <div class="feature-photo" role="img" aria-label="Calendar page with a date circled in red" style="background:linear-gradient(120deg,#e4e6ea,#9ea3ab)"></div>
    <div class="feature-text"><h3>Reminder Scheduling</h3><p>You can schedule excatly when you would like reminder messages to be sent. A lot of users use 24 hours before the appointment, another popular option is the day before at a certain time like 11am. This means the majority of replies will come in at the same time and can be dealt with in bulk.</p></div>
  </article>
  <article class="feature photo-right">
    <div class="feature-text"><h3>Appointment Replies</h3><p>We always encourage businesses to ask their clients to reply in their reminder messages. By doing this clients are showing a real commitment to show up. In January 2016 our customers had a reply rate of 30%. Of those who asked for confirmation the rate was greater than 70%.</p></div>
    <div class="feature-photo" role="img" aria-label="Business team meeting in an office" style="background:linear-gradient(120deg,#d6d2cc,#4b4744)"></div>
  </article>
  <article class="feature photo-left">
    <div class="feature-photo" role="img" aria-label="Business people shaking hands" style="background:linear-gradient(120deg,#6f88a8,#1f2f45)"></div>
    <div class="feature-text"><h3>Import Customers and Appointments</h3><p>Want to start but don't want to manually enter all your customer details and phone numbers? You can import them using our Customer Import Feaute. Same with Appointments, if you use a booking calendar that can export to a CSV file you can import this directly into our system. If you use Tessaway or Plimber Planner then this will automatically happen.</p></div>
  </article>
</section>

<section class="pricing">
  <h2 class="section-title">Pricing</h2>
  <div class="plans">
    <div class="plan"><div class="plan-name">Bronze</div><div class="plan-row">SlotNudge</div><div class="plan-row">Plimber Planner</div><div class="plan-row">Tessaway Planner</div><div class="plan-row">Free Setup</div><div class="plan-row">Backup and Restore</div><div class="plan-row plan-price">$1 / Day</div><div class="plan-order"><span>ORDER NOW</span></div></div>
    <div class="plan"><div class="plan-name">Silver</div><div class="plan-row">SlotNudge</div><div class="plan-row">Plimber Planner</div><div class="plan-row">Tessaway Planner</div><div class="plan-row">Free Setup</div><div class="plan-row">Backup and Restore</div><div class="plan-row plan-price">$2.5 / Day</div><div class="plan-order"><span>ORDER NOW</span></div></div>
    <div class="plan"><div class="plan-name">Gold</div><div class="plan-row">SlotNudge</div><div class="plan-row">Plimber Planner</div><div class="plan-row">Tessaway Planner</div><div class="plan-row">Free Setup</div><div class="plan-row">Backup and Restore</div><div class="plan-row plan-price">$4 / Day</div><div class="plan-order"><span>ORDER NOW</span></div></div>
    <div class="plan"><div class="plan-name">Platinum</div><div class="plan-row">SlotNudge</div><div class="plan-row">Plimber Planner</div><div class="plan-row">Tessaway Planner</div><div class="plan-row">Free Setup</div><div class="plan-row">Backup and Restore</div><div class="plan-row plan-price">$5 / Day</div><div class="plan-order"><span>ORDER NOW</span></div></div>
  </div>
</section>

<section class="testimonials">
  <h2 class="section-title">What Clients Say About Us</h2>
  <div class="client client-small" style="left:90px"><div class="client-photo" role="img" aria-label="Client portrait"></div><div class="client-label">Jane Porter</div></div>
  <div class="client client-small" style="left:480px"><div class="client-photo" role="img" aria-label="Client portrait"></div><div class="client-label">Tom Lee</div></div>
  <div class="client client-main"><div class="client-photo" role="img" aria-label="Client portrait"></div><div class="client-label">Dorian Vells</div></div>
  <blockquote class="quote">"Lorem ipsum dolor sit amet, consectetuer adipiscing elit, sed diam nonummy nibh euismod tincidunt ut laoreet dolore magna aliquam erat volutpat. Ut wisi enim ad minim veniam, quis nostrud exerci tation ullamcorper suscipit lobortis nisl ut aliquip ex ea commodo consequat."<cite>DORIAN VELLS</cite></blockquote>
</section>

<section class="guarantee">
  <h2 class="section-title">How Much Does A Lost Customer Cost Your Business?</h2>
  <p>SlotNudge is totally confident you'll save money using our system, we offer a full money back guarantee anytime you're not happy with our service for ANY reason.</p>
  <div class="cta-row">
    <a class="btn btn-tour" href="#">Take a Tour</a>
    <a class="btn btn-trial" href="#">Try SlotNudge for Free</a>
  </div>
</section>

<footer class="site-footer">
  <div class="footer-about">
    <p>SlotNudge is located in New Zealand. SlotNudge works in New Zealand, Australia and the United States.</p>
    <div class="flags">
      <a href="#" title="slotnudge.com.au"><svg class="flag" viewBox="0 0 40 26" role="img" aria-label="Australia site"><rect width="40" height="26" fill="#1d3c8f"/></svg></a>
      <a href="#" title="slotnudge.co.nz"><svg class="flag" viewBox="0 0 40 26" role="img" aria-label="New Zealand site"><rect width="40" height="26" fill="#1a2f7a"/></svg></a>
      <a href="#" title="slotnudge.info"><svg class="flag" viewBox="0 0 40 26" role="img" aria-label="United States site"><rect width="40" height="26" fill="#c8393f"/><rect width="40" height="4" y="5" fill="#fff"/><rect width="40" height="4" y="13" fill="#fff"/><rect width="16" height="13" fill="#2b3f86"/></svg></a>
    </div>
  </div>
  <div class="footer-col" style="left:446px"><h5>Navigation</h5><p>APPOINTMENT CALENDAR<br>PLIMBER PLANNER<br>TESSAWAY PLANNER<br>BLOG<br>CONTACT</p></div>
  <div class="footer-col" style="left:690px"><h5>Phone Support</h5><p>NEW ZEALAND : 04 555-0137<br>AUSTRALIA : 03 5550 1842<br>UNITED STATES : (602) 555-0196</p></div>
  <div class="footer-brand"><span class="brand-dot"></span><span class="brand-name">SlotNudge</span></div>
  <div class="copyright">COPYRIGHT © 2016 SLOTNUDGE. ALL RIGHTS RESERVED.</div>
</footer>

</body>
</html>
```